Digital Album Cover - Vellorin Tamsuvel Under Copper Skies (Piano & Cello)

Hi
I would like a digital album cover

Title: "Under Copper Skies (Piano & Cello)"
Artist: "Caleb Rourke & The Pell Orsola"

Preview of instrumental song:
https://tunevault-example.net/calebrourkepianist/tamsuvel-under-copper-skies-piano-and-cello

```html
<!DOCTYPE html>
<html lang="en">
<head>
<meta charset="utf-8">
<title>Under Copper Skies (Piano &amp; Cello) — Caleb Rourke &amp; The Pell Orsola</title>
<link href="https://fonts.googleapis.com/css2?family=Questrial&display=swap" rel="stylesheet">
<style>
  :root {
    --bg-deep: #0b0b0d;
    --bg-soft: #1a1b1f;
    --rule: #8c8f96;
    --frame: #b9bcc2;
    --type-light: #ffffff;
    --type-steel: #8f99a6;
    --wood-glow: #e0621f;
    --wood-mid: #8a2a0f;
    --wood-dark: #3a0e06;
  }
  html, body {
    margin: 0;
    padding: 0;
    width: 1200px;
    height: 1200px;
    overflow: hidden;
    background: var(--bg-deep);
  }
  .cover {
    position: relative;
    width: 1200px;
    height: 1200px;
    overflow: hidden;
    background:
      radial-gradient(ellipse 55% 45% at 75% 70%, var(--bg-soft) 0%, transparent 70%),
      var(--bg-deep);
    font-family: "Questrial", "Century Gothic", sans-serif;
  }
  .staff-lines {
    position: absolute;
    left: 0;
    top: 0;
  }
  .title-frame {
    position: absolute;
    left: 207px;
    top: 202px;
    width: 889px;
    height: 759px;
    border: 1px solid var(--frame);
    box-sizing: border-box;
  }
  .cello-photo {
    position: absolute;
    left: 120px;
    top: 220px;
    width: 440px;
    height: 700px;
    border-radius: 180px 180px 0 0;
    background:
      radial-gradient(ellipse 38% 28% at 45% 62%, var(--wood-glow) 0%, rgba(138,42,15,0.6) 60%, transparent 100%),
      linear-gradient(180deg, var(--wood-mid) 0%, var(--wood-dark) 70%, var(--bg-deep) 100%);
    -webkit-mask-image: linear-gradient(180deg, #000 70%, transparent 100%);
    mask-image: linear-gradient(180deg, #000 70%, transparent 100%);
  }
  .album-title {
    position: absolute;
    left: 630px;
    top: 250px;
    width: 490px;
    margin: 0;
    text-align: center;
    font-weight: 400;
    font-size: 116px;
    line-height: 140px;
    letter-spacing: -1px;
    background: linear-gradient(90deg, var(--type-light) 35%, var(--type-steel) 100%);
    -webkit-background-clip: text;
    background-clip: text;
    color: transparent;
  }
  .album-title span { display: block; }
  .album-title .title-sub {
    font-size: 40px;
    line-height: 64px;
    letter-spacing: 0.5px;
  }
  .artist-box {
    position: absolute;
    left: 144px;
    top: 1084px;
    width: 905px;
    height: 73px;
    border: 1px solid var(--frame);
    box-sizing: border-box;
    display: flex;
    align-items: center;
    justify-content: center;
  }
  .artist-credit {
    margin: 0;
    font-size: 44px;
    letter-spacing: 0.5px;
    white-space: nowrap;
    background: linear-gradient(90deg, var(--type-light) 45%, var(--type-steel) 100%);
    -webkit-background-clip: text;
    background-clip: text;
    color: transparent;
  }
</style>
</head>
<body>
  <main class="cover">
    <svg class="staff-lines" width="900" height="150" viewBox="0 0 900 150" aria-hidden="true">
      <g stroke="var(--rule)" stroke-width="1">
        <line x1="0" y1="74.5" x2="620" y2="74.5"/>
        <line x1="0" y1="85.5" x2="280" y2="85.5"/>
        <line x1="0" y1="94.5" x2="206" y2="94.5"/>
        <line x1="0" y1="112.5" x2="814" y2="112.5"/>
        <line x1="0" y1="126.5" x2="843" y2="126.5"/>
        <line x1="0" y1="141.5" x2="883" y2="141.5"/>
      </g>
    </svg>

    <div class="title-frame"></div>

    <div class="cello-photo" role="img" aria-label="Photograph of a cello body, warmly side-lit, fading into a dark background"></div>

    <h1 class="album-title">
      <span>Under</span>
      <span>Copper</span>
      <span>Skies</span>
      <span class="title-sub">(Piano &amp; Cello)</span>
    </h1>

    <div class="artist-box">
      <p class="artist-credit">Artist : Caleb Rourke &amp; The Pell Orsola</p>
    </div>
  </main>
</body>
</html>
```